IT Company Business Card Design w/Stationary Design

We have a great logo we like! We are looking to redesign our business cards and all company logo'd merchandise/materials.

We are an IT Company located near the Bay Area (San Francisco, CA). We specialize in Managed Services and offer complete IT Computer and Network Support to Businesses of all sizes. We thrive on making a lasting impression. We have been doing IT for 15yrs+ but are young at heart. We like to stand out and be different. We want to be unique and have a recognizable brand. We need our logo to represent who we are. We are young, professional, creative and outstanding. We don't want to blend in, we want to stand out. Our business card needs to stand out and grab attention. Something Bold, yet simple and clean. (I will provide ideas of what we like to give a taste of what we are looking for).

The design can include any kind of texture/artistic design or sizing EXCEPT please "no square card designs" as they don't seem to fit in wallets very well. We dont mind curved edges, rounded corners, vertical layouts or horizontal layouts, embossing, letter press or raised surfaces. Again, we dont want to look average or plain or boring. :) Be creative - yet practical! We have ordered from ZEPL designs before and been very happy. Their card sizes tend to be a little different, so beware. Hope this helps!

Target Market(s)

Businesses - Small to Medium, Corporations, Publicly Traded Companies

Industry/Entity Type

Business

Contact Information for Business Card

Harbor Circuit IT
7180 Dorrance Avenue
Suite K
Modesto, CA 95419

Office 209.555.0137
Direct 209.555.0162
Cell 209.555.0188

Gary Stroud
Founder, CEO
www.hcxit.example
gstroud@hcxit.example

Locations Serviced: Modesto, Stockton, Pleasanton, Fresno (incorporate this on the card ONLY if there's a good place to do so).

What we specialize in: Computer, Network, Voice, Data. (IT Services)

Our Logo Colors: Black and Blue (#006699). Open to using grey or orange as well - but not required. Don't want too busy....

Logo Font: "Voralyn" (Will attach logo font). We want type style to be clean. You can show different font types including our logo font - and we are open to other font ideas.

The logo can be separated. You can use elements together or apart. Surprise us! :) We "REALLY" want the "hc" to be our identifier/our brand people recognize.

Font styles to use
Sans Serif

Colors
0355a3
3176b5
f37122
f78f20
faa54b
474747
aaaaaa
757575
000000

Requirements
Must have
• Bold, Big, Colorful, Modern/yet Fun, Clean Design, Stand Out Presence, Texture would be welcomed - but not necessary, Card design shape can include cut corners or rounded or square edges. Be creative. (HOWEVER, we don't want a square design because we have found it doesn't fit in wallets that easily).
• We do like using ZEPL printing company (Which they have particular sizing on their card templates - beware), but are open to other design templates/printing companies as well. We just want to make sure its easy to find a print company to do our work. Too unique could be costly and hard to get cards printed.
• Colors to use: Our logo Blue (#006699), with either whites, grays, black, shades of our blue, and maybe a pinch of orange if needed. Primarily, blue, white, gray or black.
Nice to have
• Texture would be cool or little different edging or shape - but nothing too costly to print. I have seen cards with 3 sharp edges and one round edge. Something like that would be cool as an option. Or a vertical card.
• I love a faded watermark look. It would be nice to see some shading of our circle logo on a few designs. The circle with "hc" in it OR.... taking just the "hc" and using it alone.
Should not have
• No square card designs. Nothing too expensive or elaborate to print. No busy fonts. Do not like Times New Roman type fonts (too old looking). Not a lot of orange (if you even choose to use some orange).

```html
<!DOCTYPE html>
<html lang="en">
<head>
<meta charset="utf-8">
<title>Harbor Circuit IT – Stationery Set</title>
<link rel="stylesheet" href="https://fonts.googleapis.com/css2?family=Questrial&display=swap">
<style>
  :root {
    --brand-blue: #2b86ea;
    --brand-blue-deep: #1f6fc9;
    --charcoal: #353c3f;
    --charcoal-light: #3d474c;
    --paper: #ffffff;
    --window: #e2ebf9;
    --bg-center: #c9d3d1;
    --bg-edge: #8c9d9a;
    --silver: #d6dadc;
  }
  html, body {
    margin: 0;
    padding: 0;
    width: 1200px;
    height: 900px;
    overflow: hidden;
  }
  body {
    background: radial-gradient(circle at 48% 48%, var(--bg-center) 0%, var(--bg-edge) 75%);
    font-family: "Questrial", "Century Gothic", sans-serif;
  }
  .stationery-board { display: block; width: 1200px; height: 900px; }
  .paper { fill: var(--paper); filter: url(#drop); }
  .dark-stock { fill: var(--charcoal); filter: url(#drop); }
  .brand-dot { fill: var(--brand-blue); }
  .brand-name { fill: var(--brand-blue); font-family: "Questrial", sans-serif; }
  .brand-name--light { fill: #ffffff; }
  .fine-print { fill: var(--brand-blue); font-size: 5px; text-anchor: middle; }
  .card-print { fill: #c9d0d3; font-size: 3.6px; }
  .card-label { fill: var(--brand-blue); font-size: 3.6px; }
  .card-name { fill: #ffffff; font-size: 7px; }
  .card-title { fill: #aeb6ba; font-size: 3.8px; }
</style>
</head>
<body>
<svg class="stationery-board" viewBox="0 0 1200 900" xmlns="http://www.w3.org/2000/svg">
  <defs>
    <filter id="drop" x="-10%" y="-10%" width="120%" height="120%">
      <feDropShadow dx="0" dy="2" stdDeviation="2.5" flood-color="#000" flood-opacity="0.35"/>
    </filter>
    <clipPath id="letterhead-clip"><rect x="213" y="30" width="309" height="400"/></clipPath>
    <clipPath id="folder-clip"><rect x="661" y="27" width="296" height="405" rx="8"/></clipPath>
    <linearGradient id="card-back-fill" x1="0" y1="0" x2="1" y2="1">
      <stop offset="0" stop-color="#2b86ea"/>
      <stop offset="1" stop-color="#2a4f78"/>
    </linearGradient>
    <linearGradient id="usb-cap" x1="0" y1="0" x2="1" y2="0">
      <stop offset="0" stop-color="#b9bfc2"/>
      <stop offset="0.5" stop-color="#eef1f2"/>
      <stop offset="1" stop-color="#aab1b4"/>
    </linearGradient>
  </defs>

  <!-- Letterhead -->
  <g class="letterhead">
    <rect class="paper" x="213" y="30" width="309" height="400"/>
    <g clip-path="url(#letterhead-clip)">
      <circle class="brand-dot" cx="481" cy="74" r="45"/>
    </g>
    <text class="brand-name" x="230" y="70" font-size="14">Harbor Circuit</text>
    <text class="brand-name" x="232" y="87" font-size="8">www.hcxit.example</text>
    <text class="fine-print" x="367" y="413">Harbor Circuit IT 7180 Dorrance Avenue, Suite K Modesto, CA 95419</text>
    <text class="fine-print" x="367" y="421">Office: 209.555.0137 | Direct: 209.555.0162 | Cell: 209.555.0188</text>
  </g>

  <!-- Presentation folder -->
  <g class="folder">
    <rect class="dark-stock" x="661" y="27" width="296" height="405" rx="8"/>
    <g clip-path="url(#folder-clip)">
      <polygon points="661,27 957,27 957,235 661,335" fill="var(--charcoal-light)" role="img" aria-label="Faint repeating brand-pattern texture across the folder cover"/>
      <circle class="brand-dot" cx="908" cy="74" r="44"/>
      <path d="M957,117 C935,117 922,128 922,145 L922,210 C922,225 935,235 957,235" fill="none" stroke="#2a3033" stroke-width="1.5"/>
    </g>
  </g>

  <!-- Envelope front -->
  <g class="envelope-front">
    <rect class="paper" x="213" y="485" width="302" height="128"/>
    <circle class="brand-dot" cx="237" cy="508" r="12"/>
    <text class="brand-name" x="222" y="530" font-size="8">Harbor Circuit</text>
    <rect x="370" y="533" width="131" height="38" rx="5" fill="var(--window)" stroke="#cdd8ea" stroke-width="1"/>
    <text class="fine-print" x="364" y="602">Harbor Circuit IT 7180 Dorrance Avenue, Suite K Modesto, CA 95419</text>
    <text class="fine-print" x="364" y="608">Office: 209.555.0137 | Direct: 209.555.0162 | Cell: 209.555.0188 | www.hcxit.example</text>
  </g>

  <!-- Envelope back -->
  <g class="envelope-back">
    <rect class="paper" x="213" y="648" width="302" height="168"/>
    <path d="M213,648 L500,648 L515,666 L515,690 C495,690 490,725 470,725 L260,725 C240,725 235,690 213,690 Z" fill="var(--charcoal)"/>
    <line x1="364" y1="650" x2="364" y2="725" stroke="#2c3235" stroke-width="1"/>
  </g>

  <!-- Business card front -->
  <g class="business-card-front">
    <path class="dark-stock" d="M662,507 L776,507 Q786,507 786,517 L786,579 L662,579 Z"/>
    <text class="card-label" x="669" y="516">Phone</text>
    <text class="card-print" x="669" y="521">Office 209.555.0137</text>
    <text class="card-print" x="669" y="525">Direct 209.555.0162</text>
    <text class="card-print" x="669" y="529">Cell 209.555.0188</text>
    <text class="card-label" x="669" y="536">Address</text>
    <text class="card-print" x="669" y="541">Harbor Circuit IT</text>
    <text class="card-print" x="669" y="545">7180 Dorrance Ave, Suite K</text>
    <text class="card-print" x="669" y="549">Modesto, CA 95419</text>
    <text class="card-label" x="669" y="556">Online</text>
    <text class="card-print" x="669" y="561">www.hcxit.example</text>
    <text class="card-print" x="669" y="565">gstroud@hcxit.example</text>
    <circle class="brand-dot" cx="758" cy="522" r="12"/>
    <text class="brand-name brand-name--light" x="737" y="546" font-size="8">Harbor Circuit</text>
    <text class="card-name" x="738" y="569">Gary Stroud</text>
    <text class="card-title" x="738" y="574">Founder, CEO</text>
  </g>

  <!-- Business card back -->
  <g class="business-card-back">
    <path d="M829,507 L942,507 Q952,507 952,517 L952,579 L829,579 Z" fill="url(#card-back-fill)" filter="url(#drop)" role="img" aria-label="Card back covered in a blue repeating brand pattern on charcoal"/>
  </g>

  <!-- CD disc and sleeve -->
  <g class="disc-pack">
    <circle cx="843" cy="740" r="82" fill="var(--brand-blue)" filter="url(#drop)"/>
    <circle cx="843" cy="740" r="40" fill="none" stroke="var(--brand-blue-deep)" stroke-width="3"/>
    <rect class="dark-stock" x="630" y="659" width="190" height="162" role="img" aria-label="Sleeve with faint repeating brand-pattern texture"/>
    <circle class="brand-dot" cx="762" cy="706" r="46"/>
    <circle cx="830" cy="740" r="14" fill="#2f3538"/>
    <circle cx="830" cy="740" r="10" fill="var(--silver)"/>
    <circle cx="830" cy="740" r="5" fill="#ffffff"/>
  </g>

  <!-- USB drive -->
  <g class="usb-drive">
    <rect x="946" y="700" width="22" height="20" rx="3" fill="url(#usb-cap)"/>
    <rect x="940" y="716" width="34" height="51" rx="5" fill="#f3f5f6" filter="url(#drop)"/>
    <circle class="brand-dot" cx="957" cy="749" r="10"/>
  </g>
</svg>
</body>
</html>
```